ALL TEXT Social Media Graphics

We are looking for a series of social media graphics for Instagram (new size: 4:5 (1080 x 1350 pixels) ratio that are ALL TEXT. We want the following quotes below on each graphic; one quote per graphic. AND, In very small letters at the bottom of each graphic, add @PaulaWrenLive
The look and feel of these graphics should be complimentary to the color palette attached below; but keep them simple. But the design is up to you; at the end of this document, I provided various samples of all text graphics that I like as examples.
The Quotes are in the attached WORD document
women trying to lose weight

```html
<!DOCTYPE html>
<html lang="en">
<head>
<meta charset="utf-8">
<title>Summer Reset – Text Post Series</title>
<link rel="stylesheet" href="https://fonts.googleapis.com/css2?family=Figtree:wght@900&family=Poppins:wght@300;400;500&display=swap">
<style>
  :root {
    --backdrop: #fbb3ca;
    --card-light: #fde5ec;
    --magenta: #ae1456;
    --rose: #ec5f97;
    --rose-soft: #f9bfd5;
    --ink: #262626;
    --shadow: 0 8px 18px rgba(150, 40, 80, 0.28);
  }
  * { margin: 0; padding: 0; box-sizing: border-box; }
  html, body {
    width: 1200px; height: 824px; overflow: hidden;
    background: var(--backdrop);
  }
  .canvas { position: relative; width: 1200px; height: 824px; }

  .post {
    position: absolute; top: 193px;
    width: 350px; height: 437px;
    background: var(--card-light);
    box-shadow: var(--shadow);
  }
  .post--left { left: 44px; }
  .post--center { left: 425px; background: var(--magenta); }
  .post--right { left: 807px; }

  .headline {
    position: absolute;
    font-family: "Figtree", sans-serif;
    font-weight: 900;
    font-size: 27px;
    line-height: 32px;
    letter-spacing: -0.2px;
    color: var(--magenta);
  }
  .promise {
    position: absolute;
    font-family: "Poppins", sans-serif;
    font-weight: 300;
    font-size: 25px;
    line-height: 32px;
    color: var(--rose);
  }
  .cta {
    position: absolute;
    font-family: "Poppins", sans-serif;
    font-weight: 300;
    font-size: 19px;
    line-height: 24px;
    color: var(--ink);
  }
  .cta strong {
    font-family: "Figtree", sans-serif;
    font-weight: 900;
    color: var(--magenta);
  }
  .handle {
    position: absolute;
    font-family: "Poppins", sans-serif;
    font-weight: 400;
    font-size: 9.5px;
    color: var(--ink);
  }

  /* left card: left aligned */
  .post--left .headline { left: 24px; top: 40px; }
  .post--left .promise { left: 24px; top: 168px; }
  .post--left .cta { left: 24px; top: 302px; }
  .post--left .handle { right: 37px; top: 407px; }

  /* center card: centered */
  .post--center .headline,
  .post--center .promise,
  .post--center .cta,
  .post--center .handle { left: 0; right: 0; text-align: center; }
  .post--center .headline { top: 40px; color: var(--card-light); }
  .post--center .promise { top: 168px; color: var(--rose-soft); }
  .post--center .cta { top: 302px; color: var(--card-light); }
  .post--center .cta strong { color: var(--card-light); }
  .post--center .handle { top: 407px; color: var(--rose-soft); }

  /* right card: right aligned */
  .post--right .headline { right: 23px; top: 27px; text-align: right; }
  .post--right .promise { right: 23px; top: 155px; text-align: right; }
  .post--right .cta { right: 23px; top: 289px; text-align: right; }
  .post--right .handle { left: 24px; top: 411px; }
</style>
</head>
<body>
<main class="canvas">
  <article class="post post--left">
    <h2 class="headline">You can absolutely be<br>down 20–30 pounds by<br>end of summer.</h2>
    <p class="promise">All it takes is the<br>right plan—and<br>you’ve found it.</p>
    <p class="cta">Comment <strong>“Bright Girl”</strong> for the<br>Bright Girl Summer Reset!</p>
    <p class="handle">@PaulaWrenLive</p>
  </article>

  <article class="post post--center">
    <h2 class="headline">You don’t need another<br>diet — you need a<br>system that works.</h2>
    <p class="promise">Drop 30 pounds with<br>the Bright Girl<br>Summer Reset.</p>
    <p class="cta">Comment <strong>“Summer”</strong> to<br>start now.</p>
    <p class="handle">@PaulaWrenLive</p>
  </article>

  <article class="post post--right">
    <h2 class="headline">This summer ain’t<br>over—and neither<br>are your body goals.</h2>
    <p class="promise">Drop 30 pounds<br>with the Bright Girl<br>Summer Reset.</p>
    <p class="cta">Comment <strong>“Bright Girl”</strong><br>to get the plan</p>
    <p class="handle">@PaulaWrenLive</p>
  </article>
</main>
</body>
</html>
```